Website Design for Business Law Firm

We have a logo and now we would like a web site design for our new website. Our small firm provides creative and aggressive transactional (not litigation) legal services to advise healthcare, technology, internet-based and traditional companies and investors in such companies on healthcare, technology, financing, mergers/acquisitions, real estate and other transactions, legal compliance and general corporate and business matters.

We would like to see a website design that is professional and appropriate for executives, professionals, investors and government regulators to visit, that conveys professionalism and competence while being a little edgy and modern - no typical legal motifs such as gavels, books, or scales of justice. We advise businesses and investors and guide them through complicated issues quickly, capably and differently from other law firms. We are part of the business team and get things done.

The logo is attached, and we like gray as a color to complement it. The intention of the logo is to convey that in a storm or challenging time, people come to this firm, and people come to this firm when they need the power and disruption to change things or shake them up.

I have also enclosed a picture of our business card for consideration.

On the other hand, you can check out the current simple site at www.venhollow.example to see we have used a space motif in the past to evoke that we help create stars (the nebula featured there). This is not a necessary part of the new website and it may look better without it.

We appreciate your creativity and look forward to designs.

Industry/Entity Type

Business

Requirements
Must have
• We anticipate the following pages, and you may submit different ideas for the different pages:
• 1. Landing page
• 2. Services pages - healthcare, IT/Technology, general counsel services, financings, mergers/acquisitions, mediation/arbitration, procurement and productization
• 3. About Us including contact information
• Our name and contact information:
• Quellane Law Firm, P.C.
• 8716 SW 19th Ave.
• Portland, OR 97213
• phone: 971.555.0143
• fax: 971.555.0187
Nice to have
• Please consider designs that enhance the impressions we are looking for
Should not have
• Please no gavels, scales of justice, law books, or similar traditional legal imagery.

```html
<!DOCTYPE html>
<html lang="en">
<head>
<meta charset="utf-8">
<title>Quellane Law Firm, P.C.</title>
<link rel="stylesheet" href="https://fonts.googleapis.com/css2?family=Arimo:wght@400;700&family=PT+Sans:wght@400&display=swap">
<style>
:root{
  --band:#ededed;
  --page:#ffffff;
  --ink:#1c1c1c;
  --body:#3a3a3a;
  --muted:#555555;
  --rule:#dcdcdc;
  --purple:#5b2a86;
  --purple-top:#6b2f9b;
  --purple-bottom:#4c176c;
  --purple-edge:#8c55c2;
  --purple-soft:#b89ad8;
  --photo-sky:#e9a8a0;
  --photo-dusk:#5f6478;
  --photo-ground:#1a1a1e;
  --wood:#7a3b22;
  --wood-light:#c9b8a8;
  --footer:#f4f3f4;
}
*{margin:0;padding:0;box-sizing:border-box}
html,body{width:1200px;height:1045px;overflow:hidden;background:var(--page)}
body{position:relative;font-family:"Arimo",Helvetica,Arial,sans-serif;color:var(--body)}
.top-band{position:absolute;left:0;top:0;width:1200px;height:421px;background:var(--band)}
.brand{position:absolute;left:70px;top:30px;font-size:54px;letter-spacing:14px;color:var(--ink);font-weight:400}
.main-nav{position:absolute;left:714px;top:56px;display:flex;height:67px}
.main-nav a{display:flex;align-items:center;padding:0 18px;font-size:19px;color:var(--purple);text-decoration:none;border-left:1px solid var(--rule);height:67px;padding-bottom:4px}
.main-nav a:first-child{border-left:none}
.hero{position:absolute;left:67px;top:121px;width:1067px;height:423px;background:#fff;border:1px solid var(--rule);border-radius:4px}
.hero-photo{position:absolute;left:9px;top:9px;width:731px;height:405px;border-radius:4px 0 0 4px;background:linear-gradient(180deg,var(--photo-dusk) 0%,#8e7d8c 20%,var(--photo-sky) 45%,#c99892 65%,var(--photo-ground) 100%)}
.hero-panel{position:absolute;left:740px;top:9px;width:317px;height:405px;border-radius:0 4px 4px 0;border-left:4px solid var(--purple-edge);background:linear-gradient(180deg,var(--purple-top),var(--purple-bottom));font-family:"PT Sans",Arial,sans-serif;color:#fff;padding:60px 0 0 32px}
.hero-kicker{font-size:21px;color:var(--purple-soft);line-height:26px}
.hero-title{font-size:28px;line-height:31px;font-weight:400;margin-top:2px}
.hero-text{font-size:13px;line-height:22.5px;margin-top:11px;width:255px;color:#f3ecf8}
.dots{display:flex;gap:4px;margin-top:14px;margin-left:4px}
.dots span{width:13px;height:13px;border-radius:50%;background:#9a72c4}
.dots span:first-child{background:#fff}
.column{position:absolute;top:593px}
.col-about{left:76px;width:330px}
.col-services{left:458px;width:300px}
.col-invest{left:795px;width:320px}
.divider{position:absolute;top:601px;width:1px;height:251px;background:var(--rule)}
h2{font-size:24px;font-weight:400;color:var(--ink);line-height:32px}
h2 b{font-weight:700}
.lead{font-size:14px;font-weight:700;color:var(--ink);line-height:25px;margin-top:13px}
.copy{font-size:14px;line-height:25.5px;margin-top:6px;color:var(--body)}
.service-list{list-style:none;margin-top:12px}
.service-list li{position:relative;padding-left:14px;font-size:14px;color:var(--purple);letter-spacing:.3px;line-height:31px}
.service-list li::before{content:"";position:absolute;left:14px;top:11px;border-left:5px solid var(--purple);border-top:5px solid transparent;border-bottom:5px solid transparent}
.service-list li{padding-left:28px}
.office-photo{width:317px;height:133px;margin-top:14px;background:linear-gradient(90deg,var(--wood) 0%,#a25a34 45%,var(--wood-light) 70%,#8b4a2b 100%)}
.col-invest .lead{margin-top:9px;font-weight:400;color:var(--ink)}
.col-invest .copy{margin-top:0;font-size:14px}
.site-footer{position:absolute;left:0;top:936px;width:1200px;height:109px;border-top:1px solid var(--rule);background:linear-gradient(180deg,var(--footer),#fbfafb)}
.social{position:absolute;left:86px;top:27px;display:flex;gap:6px}
.social span{width:20px;height:20px;border-radius:50%;background:#6e6e6e}
.footer-nav{position:absolute;left:171px;top:28px;font-size:13px;color:var(--muted)}
.footer-nav a{color:var(--muted);text-decoration:none}
.footer-nav i{font-style:normal;margin:0 6px}
.legal{position:absolute;right:94px;top:28px;font-size:12.5px;color:var(--muted)}
</style>
</head>
<body>
<div class="top-band"></div>
<div class="brand">QUELLANE</div>
<nav class="main-nav">
  <a href="#">Home</a><a href="#">About us</a><a href="#">Services</a><a href="#">Contact</a>
</nav>

<section class="hero">
  <div class="hero-photo" role="img" aria-label="Photograph of a city skyline with glass towers at dusk under a pink sky"></div>
  <div class="hero-panel">
    <p class="hero-kicker">We Provide Services to</p>
    <h1 class="hero-title">Corporate and<br>Institutional Investors</h1>
    <p class="hero-text">Nunc tempus felis vitae urna. Vivamus portti-tor, g, purus nisi eleifend libero, a tempus libero lectus feugiat felis. Morbi diam mauris, viverra in, gravida eu, mattis in, ante. Morbi eget arcu. Morbi porta, libero id</p>
    <div class="dots"><span></span><span></span><span></span></div>
  </div>
</section>

<section class="column col-about">
  <h2><b>About</b> Quellane Lawyers</h2>
  <p class="lead">Nunc tempus felis vitae urna. purus nisi eleifend libero, a tempus libero lectus feugiat felis.</p>
  <p class="copy">Morbi eget arcu. Morbi porta, libero id ullamcorper diam nonummy nibh euismod tincidunt ut laoreet dolore magna aliquam erat volutpat. Ut wisi enim ad minim veniam, quis nostrud exerci tation ullamcorper suscipit lobortis nisl ut aliquip ex ea commodo consequat. Duis autem vel eum.</p>
</section>
<div class="divider" style="left:428px"></div>

<section class="column col-services">
  <h2><b>Services</b> We Provide</h2>
  <p class="lead">Vivamus portitorpurus nisi elefend libero, a tempus livero lectus feugiat felis.</p>
  <ul class="service-list">
    <li>CONSECTETUER ADIPISCING</li>
    <li>DO EIUSMOD TEMPOR</li>
    <li>ALIQUAM ERAT VOLUTPAT</li>
    <li>DUIS AUTEM VEL EUM</li>
    <li>BLANDIT PRAESENT</li>
  </ul>
</section>
<div class="divider" style="left:756px"></div>

<section class="column col-invest">
  <h2>Local Foregin Investment</h2>
  <div class="office-photo" role="img" aria-label="Photograph of a modern office lobby with wood-panelled walls and a reception desk"></div>
  <p class="lead">Lorem ipsum dolor sit amet.</p>
  <p class="copy">Vivamus portitor, g, purus nisi elefend libero, a tempus livero lectus feugiat felis.</p>
</section>

<footer class="site-footer">
  <div class="social" aria-label="Social links"><span></span><span></span><span></span></div>
  <nav class="footer-nav"><a href="#">Home</a><i>/</i><a href="#">About Us</a><i>/</i><a href="#">Services</a><i>/</i><a href="#">Contact</a></nav>
  <p class="legal">© 2014 Quellane Law. All rights reserved. Terms of Use</p>
</footer>
</body>
</html>
```